Simplified minimalist but bold website

Design a website for a brand 'Brighten Each Morning' that shares ideas to make managing home and health easier through email swap series, webinars and eventually courses.

Simple landing page to attract users to sign up for a freebie.

Target Market(s)

women with families & homes to run

Number of Pages Required

1 page

Font styles to use
Sans Serif

Colors
e667a6
b768aa
acd136
ffffff
959595

Requirements
Must have
• Simplified look, line icons, opt-in template, contact us form

```html
<!DOCTYPE html>
<html lang="en">
<head>
<meta charset="utf-8">
<title>Brighten Each Morning</title>
<link href="https://fonts.googleapis.com/css2?family=Mulish:wght@400;600;700&family=Open+Sans:wght@400;600;700&display=swap" rel="stylesheet">
<style>
:root{
  --blue:#2b93cf;
  --purple:#a8519c;
  --lime:#cde829;
  --green:#9ccb2c;
  --pink:#e0509a;
  --plum:#b35aa0;
  --ink:#333;
  --footer:#2b2b2b;
  --white:#fff;
  --hero-sky:#dde8ea;
  --hero-mid:#a9c4cc;
  --hero-warm:#c4a792;
}
*{box-sizing:border-box;margin:0;padding:0}
html,body{width:781px;height:1200px;overflow:hidden;background:var(--white)}
body{font-family:"Open Sans",Arial,sans-serif;color:var(--ink);position:relative}
.heading{font-family:"Mulish",Arial,sans-serif}

.hero{position:absolute;left:0;top:0;width:781px;height:400px;overflow:hidden}
.hero-photo{position:absolute;inset:0;
  background:linear-gradient(180deg,var(--hero-sky) 0%,var(--hero-mid) 55%,var(--hero-warm) 100%)}
.hero-title{position:absolute;top:18px;left:0;width:100%;text-align:center;font-size:32px;font-weight:700;color:var(--blue);
  text-shadow:0 0 6px rgba(255,255,255,.8)}
.hero-sub{position:absolute;top:65px;left:0;width:100%;text-align:center;font-size:16px;line-height:21px;color:var(--plum);
  text-shadow:0 0 5px rgba(255,255,255,.9)}
.scroll-cue{position:absolute;left:381px;top:378px}

.panel{position:absolute;top:400px;height:476px;width:390.5px}
.panel-swaps{left:0;background:var(--blue)}
.panel-guide{left:390.5px;background:var(--purple)}

.col-left{left:99px;width:266px}
.col-right{left:416px;width:266px}
.kicker{position:absolute;top:449px;font-size:10.5px;color:var(--white);text-align:center;white-space:nowrap}
.panel-title{position:absolute;top:466px;font-size:22px;font-weight:700;color:var(--lime);text-align:center;white-space:nowrap}
.rule{position:absolute;top:509px;width:52px;height:2px;background:var(--white)}
.lead{position:absolute;left:90px;width:284px;top:528px;font-size:11px;font-weight:600;line-height:15px;text-align:center;color:var(--white)}
.small{position:absolute;left:0;width:462px;top:564px;font-size:8px;line-height:14.5px;text-align:center;color:var(--white)}
.ghost-btn{position:absolute;top:620px;height:33px;width:130px;border:1.5px solid var(--white);
  font-family:"Mulish",Arial,sans-serif;font-size:11px;font-weight:600;line-height:30px;color:var(--white);text-align:center}
.prompt{position:absolute;top:683px;font-size:11px;font-weight:600;text-align:center;color:var(--white)}
.field{position:absolute;height:31px;width:266px;background:var(--white);color:#555;font-size:9px;
  line-height:31px;text-align:left;padding-left:15px}
.cta{position:absolute;height:31px;width:266px;background:var(--green);color:var(--white);
  font-size:10.5px;font-weight:700;line-height:31px;text-align:center}
.guide-cover{position:absolute;left:436px;top:525px;width:228px;height:165px}

.details{position:absolute;top:876px;left:0;width:781px;height:272px;text-align:center}
.details-title{position:absolute;top:28px;left:0;width:100%;font-size:22px;font-weight:600;color:var(--blue)}
.details-text{position:absolute;left:0;width:100%;font-size:8px;line-height:14.6px;color:#222}
.details-note{position:absolute;top:128px;left:0;width:100%;font-size:11.5px;line-height:18px;color:var(--plum)}
.cta-pink{position:absolute;left:257px;top:208px;width:266px;height:31px;background:var(--pink);color:var(--white);
  font-size:10.5px;font-weight:700;line-height:31px}

.footer{position:absolute;top:1148px;left:0;width:781px;height:52px;background:var(--footer)}
.copyright{position:absolute;left:94px;top:20px;font-size:7.5px;color:#aaa}
.social{position:absolute;top:20px;width:10px;height:10px;border-radius:50%;background:#8a8a8a}
</style>
</head>
<body>
<header class="hero">
  <div class="hero-photo" role="img" aria-label="Photo of a smiling woman relaxing on cushions outdoors"></div>
  <h1 class="hero-title heading">Brighten Each Morning.</h1>
  <p class="hero-sub heading">Chances are life is a little overwhelming.<br>Let us help</p>
  <svg class="scroll-cue" width="19" height="12" viewBox="0 0 19 12" aria-hidden="true">
    <polyline points="2,2 9.5,9 17,2" fill="none" stroke="#333" stroke-width="2.5"/>
  </svg>
</header>

<section class="panel panel-swaps"></section>
<section class="panel panel-guide"></section>

<p class="kicker heading col-left">Baby Steps... (try out a few of our tricks)</p>
<h2 class="panel-title heading col-left">Swaps Email Series</h2>
<div class="rule" style="left:216px"></div>
<p class="lead">Save TIME, MONEY and SANITY with simple product swaps.</p>
<p class="small">Reduce the amount of work it takes to run your home.<br>Swap out existing products for more sustainable ones.<br>Each swap saves you work, clutter, time &amp; money.</p>
<div class="ghost-btn" style="left:99px">SEE SAMPLE SWAP</div>
<div class="ghost-btn" style="left:235px">LEARN MORE</div>
<p class="prompt col-left">Send your ideas my way...</p>
<div class="field" style="left:99px;top:710px">Name</div>
<div class="field" style="left:99px;top:751px">Email</div>
<div class="cta" style="left:99px;top:793px">SEND ME THE GUIDE!</div>

<p class="kicker heading col-right">Big Leap... (I'm ready to roll up my sleeves)</p>
<h2 class="panel-title heading col-right">Decluttering Guide</h2>
<div class="rule" style="left:523px"></div>
<svg class="guide-cover" viewBox="0 0 228 165" role="img" aria-label="Two printed guide booklet covers with photos">
  <rect x="112" y="14" width="108" height="146" fill="#eef3f3" transform="rotate(4 166 87)"/>
  <rect x="16" y="10" width="100" height="146" fill="#d9cfc6" transform="rotate(-18 66 83)"/>
</svg>
<div class="field" style="left:416px;top:710px">Name</div>
<div class="field" style="left:416px;top:751px">Email</div>
<div class="cta" style="left:416px;top:793px">SIGN ME UP!</div>

<section class="details">
  <h2 class="details-title heading">Swaps Email Series</h2>
  <p class="details-text" style="top:62px">Save TIME, MONEY and SANITY with simple product swaps.<br>And reduce the amount of work it takes to run your home.<br>Swap out existing products for more sustainable ones.<br>Each swap save you work, clutter, time &amp; money.</p>
  <p class="details-note heading">You get an email&nbsp; 2x weekly for 6-12 weeks only<br>Get even more if you feel they are helpful to you</p>
  <p class="details-text" style="top:172px">Join our monthly SIMPLE SWAP SHARING web jams with other mums and get even more ideas.<br>Better yet, come with great tips of your own to share.</p>
  <div class="cta-pink">SIGN ME UP!</div>
</section>

<footer class="footer">
  <p class="copyright">Copyright &copy;&nbsp; 2018&nbsp; Brighten Each Morning.&nbsp; All rights reserved.</p>
  <span class="social" style="left:652px" aria-label="Social link"></span>
  <span class="social" style="left:675px" aria-label="Social link"></span>
</footer>
</body>
</html>
```